business card design

i would like business cards designed. My business provides trade qualified personnel to the mining industry to work on heavy mobile equipment.
please put a excavator(digger) in the background in one design and have one design without so i can compare the difference.
also add info:
my logo(attached) and "mobile equipment repair and maintenance"
name: Gavin Stroud
address: 42 Brindle RD Lowmere Ashvale WA.
mobile: 0461902738
email: gavin@hollowvex.com

```html
<!DOCTYPE html>
<html lang="en">
<head>
<meta charset="utf-8">
<title>Hollowvex Business Card</title>
<link rel="stylesheet" href="https://fonts.googleapis.com/css2?family=Arimo:wght@400;700&display=swap">
<style>
  :root {
    --bg: #e4e3e1;
    --card-white: #f7f7f7;
    --navy: #0b1e3f;
    --navy-deep: #061530;
    --navy-mid: #0f2a55;
    --brand-blue: #1565d8;
    --brand-dim: #163a73;
    --text-grey: #5a5d63;
    --rule-grey: #7b7e83;
    --tagline: #dfe4ec;
  }
  * { box-sizing: border-box; margin: 0; padding: 0; }
  html, body {
    width: 1200px;
    height: 801px;
    overflow: hidden;
    background: var(--bg);
    font-family: "Arimo", Arial, sans-serif;
  }
  .stage {
    position: relative;
    width: 1200px;
    height: 801px;
    display: flex;
    align-items: center;
    justify-content: center;
    gap: 44px;
  }
  .card {
    position: relative;
    width: 540px;
    height: 328px;
    border-bottom: 4px solid var(--brand-blue);
    box-shadow: 0 10px 24px rgba(0, 0, 0, 0.18);
    overflow: hidden;
  }

  /* Front */
  .card--front { background: var(--card-white); }
  .brand {
    position: absolute;
    display: flex;
    align-items: center;
    gap: 10px;
    white-space: nowrap;
  }
  .brand__mark {
    width: 16px;
    height: 16px;
    background: var(--brand-blue);
    flex: none;
  }
  .brand__name {
    font-weight: 700;
    letter-spacing: 2px;
  }
  .card--front .brand { top: 58px; left: 156px; }
  .card--front .brand__name { font-size: 40px; color: var(--navy); }
  .address {
    position: absolute;
    right: 36px;
    top: 148px;
    font-size: 16px;
    line-height: 21px;
    color: var(--text-grey);
    white-space: nowrap;
  }
  .holder-name {
    position: absolute;
    left: 40px;
    top: 176px;
    font-size: 21px;
    font-weight: 700;
    letter-spacing: 0.5px;
    text-transform: uppercase;
    color: var(--brand-blue);
    white-space: nowrap;
  }
  .divider {
    position: absolute;
    left: 34px;
    right: 34px;
    top: 208px;
    height: 1px;
    background: var(--rule-grey);
  }
  .contacts {
    position: absolute;
    left: 40px;
    top: 224px;
    list-style: none;
    font-size: 16px;
    color: var(--text-grey);
  }
  .contacts__item {
    display: flex;
    align-items: center;
    gap: 10px;
    height: 26px;
    white-space: nowrap;
  }
  .contacts__icon { width: 14px; height: 14px; flex: none; }

  /* Back */
  .card--back {
    background: radial-gradient(ellipse at 70% 20%, var(--navy-mid) 0%, var(--navy) 45%, var(--navy-deep) 100%);
  }
  .card--back .brand {
    top: 110px;
    left: 50%;
    transform: translateX(-50%);
  }
  .card--back .brand__mark { background: var(--brand-dim); }
  .card--back .brand__name { font-size: 44px; color: var(--brand-dim); }
  .tagline {
    position: absolute;
    left: 0;
    right: 0;
    top: 236px;
    text-align: center;
    font-size: 17px;
    color: var(--tagline);
    letter-spacing: 0.3px;
  }
</style>
</head>
<body>
<main class="stage">
  <section class="card card--front" aria-label="Business card front">
    <div class="brand">
      <span class="brand__mark"></span>
      <span class="brand__name">HOLLOWVEX</span>
    </div>
    <p class="address">42 Brindle RD<br>Lowmere Ashvale WA.</p>
    <h1 class="holder-name">Gavin Stroud</h1>
    <div class="divider"></div>
    <ul class="contacts">
      <li class="contacts__item">
        <svg class="contacts__icon" viewBox="0 0 24 24" aria-hidden="true">
          <path fill="#1565d8" d="M6.6 10.8a15.1 15.1 0 0 0 6.6 6.6l2.2-2.2c.3-.3.7-.4 1-.2 1.1.4 2.3.6 3.6.6.6 0 1 .4 1 1V20c0 .6-.4 1-1 1A17 17 0 0 1 3 4c0-.6.4-1 1-1h3.5c.6 0 1 .4 1 1 0 1.3.2 2.5.6 3.6.1.3 0 .7-.2 1z"/>
        </svg>
        <span>0461902738</span>
      </li>
      <li class="contacts__item">
        <svg class="contacts__icon" viewBox="0 0 24 24" aria-hidden="true">
          <rect x="2" y="5" width="20" height="14" fill="#1565d8"/>
          <path d="M2 5l10 8 10-8" fill="none" stroke="#f7f7f7" stroke-width="1.6"/>
        </svg>
        <span>gavin@hollowvex.com</span>
      </li>
    </ul>
  </section>

  <section class="card card--back" aria-label="Business card back">
    <div class="brand">
      <span class="brand__mark"></span>
      <span class="brand__name">HOLLOWVEX</span>
    </div>
    <p class="tagline">Mobile Equipment Repair And Maintenance</p>
  </section>
</main>
</body>
</html>
```